Renata Quisby

Luxury And Style -

Black - White & Gold

Target Market(s)

Fashion

Industry/Entity Type

Fashion

Requirements
Must have
• High-End
Nice to have
• We will Print on Silk Paper

```html
<!DOCTYPE html>
<html lang="en">
<head>
<meta charset="utf-8">
<title>Renata Quisby — Letterhead</title>
<link href="https://fonts.googleapis.com/css2?family=Marcellus&family=Poppins:wght@300&display=swap" rel="stylesheet">
<style>
  :root {
    --navy: #252240;
    --gold: #c19c6f;
    --ink: #000000;
    --paper: #ffffff;
  }
  html, body {
    margin: 0;
    padding: 0;
    overflow: hidden;
    background: var(--paper);
  }
  .letterhead {
    position: relative;
    width: 848px;
    height: 1200px;
    background: var(--paper);
    overflow: hidden;
  }
  .letterhead__shapes {
    position: absolute;
    inset: 0;
    width: 848px;
    height: 1200px;
  }
  .band { fill: var(--navy); }
  .accent-wave { fill: var(--gold); stroke: var(--paper); stroke-width: 5; }
  .accent-dot { fill: var(--ink); }
  .brand {
    position: absolute;
    left: 90px;
    top: 150px;
    width: 240px;
    text-align: center;
    color: var(--navy);
  }
  .brand__name {
    margin: 0;
    font-family: "Marcellus", serif;
    font-weight: 400;
    font-size: 26px;
    letter-spacing: 3px;
    line-height: 1.2;
    text-transform: uppercase;
    white-space: nowrap;
  }
  .brand__tagline {
    margin: 14px 0 0;
    font-family: "Poppins", sans-serif;
    font-weight: 300;
    font-size: 12.5px;
    letter-spacing: 0.3px;
    text-transform: uppercase;
  }
</style>
</head>
<body>
  <div class="letterhead">
    <svg class="letterhead__shapes" viewBox="0 0 848 1200" xmlns="http://www.w3.org/2000/svg" aria-hidden="true">
      <path class="accent-wave" d="M583,-4 L852,-4 L852,210 C760,206 700,160 668,84 C650,38 622,10 583,-4 Z"/>
      <path class="band" d="M0,0 L540,0 C590,0 622,25 645,75 L72,75 C30,75 4,40 0,0 Z"/>
      <circle class="accent-dot" cx="629" cy="132" r="15"/>
      <path class="band" d="M0,1200 C4,1148 52,1115 105,1115 L747,1115 C800,1115 842,1148 848,1200 Z"/>
    </svg>
    <header class="brand">
      <h1 class="brand__name">Renata Quisby</h1>
      <p class="brand__tagline">Luxury and Style</p>
    </header>
  </div>
</body>
</html>
```